Breezy Burro Menu Design for new restaurant

Need a menu design for new restaurant- Fast Casual Taqueria. I have the files for our logo and menu already completed. Let me know what type of file your require and I can send it with regard to my logo. I want it to be easy to read but on a half page rack size type card, front and back. Simple and to the point but important to include the items listed with ingredients. Feel free to use icons for different categories.

Target Market(s)

Any one who loves tacos and margaritas...fun...festive...casual...

Font styles to use
Other font styles liked:
• lobster 1.3 and farmer round

Colors
3276b5
ec1f27
ffffff
85cae6
9bcb3c
fbed22

Requirements
Must have
• Designed for a half page, front and back (4.25 x 11). NO full size page menu. Easy to read. Not complicated. Use our logo. I need to be able to modify the menu from my end with out any special software.
Nice to have
• Fun~Festive~ color. Stick with our logo theme using our font lobster 1.3 and farmer round.
Should not have
• Full page format. Do not want stock food phots. Just graphics or icons.

```html
<!DOCTYPE html>
<html lang="en">
<head>
<meta charset="utf-8">
<title>Breezy Burro Menu</title>
<link rel="stylesheet" href="https://fonts.googleapis.com/css2?family=Antonio:wght@700&family=IBM+Plex+Mono:wght@400;700&family=Lobster&display=swap">
<style>
  :root {
    --paper: #f6fbd5;
    --red: #ef1a2d;
  }
  * { margin: 0; padding: 0; box-sizing: border-box; }
  html, body { width: 1200px; height: 2934px; overflow: hidden; background: var(--paper); }
  .menu-card {
    position: relative;
    width: 1200px;
    height: 2934px;
    background: var(--paper);
    color: var(--red);
    font-family: "IBM Plex Mono", monospace;
  }
  .frames { position: absolute; inset: 0; }
  .title-word {
    font-family: "Antonio", sans-serif;
    font-weight: 700;
    fill: var(--red);
  }
  .script {
    position: absolute;
    font-family: "Lobster", cursive;
    color: var(--red);
    white-space: nowrap;
    transform-origin: left bottom;
  }
  .script-intro-1 { left: 468px; top: 378px; font-size: 72px; transform: rotate(-9deg); }
  .script-intro-2 { left: 584px; top: 440px; font-size: 72px; transform: rotate(-9deg); }
  .script-tacos { left: 208px; top: 1756px; font-size: 118px; transform: rotate(-5deg); }
  .item {
    position: absolute;
    left: 148px;
    width: 920px;
    font-size: 25px;
    line-height: 39px;
    letter-spacing: 0.2px;
  }
  .tacos .item { left: 146px; }
  .item-name {
    font-family: "Antonio", sans-serif;
    font-weight: 700;
    font-size: 52px;
    line-height: 0;
    margin-right: 8px;
    letter-spacing: 0.5px;
  }
  .upcharge {
    display: block;
    text-align: right;
    font-weight: 700;
    margin-right: -20px;
  }
  .tacos-note {
    position: absolute;
    left: 531px;
    top: 1884px;
    font-size: 18px;
    line-height: 22px;
    font-weight: 700;
  }
  .brand-name {
    position: absolute;
    left: 434px;
    width: 332px;
    top: 2800px;
    text-align: center;
    font-family: "Antonio", sans-serif;
    font-weight: 700;
    font-size: 38px;
    color: var(--red);
  }
</style>
</head>
<body>
<main class="menu-card">
  <svg class="frames" width="1200" height="2934" viewBox="0 0 1200 2934" aria-hidden="true">
    <text class="title-word" x="376" y="333" font-size="300" textLength="447" lengthAdjust="spacingAndGlyphs">MENU</text>
    <g fill="none" stroke="var(--red)" stroke-width="3">
      <polyline points="434,450 105,450 105,1809 182,1809"/>
      <polyline points="1018,450 1094,450 1094,1809 575,1809"/>
      <polyline points="180,1860 105,1860 105,2830 434,2830"/>
      <polyline points="530,1860 1094,1860 1094,2830 766,2830"/>
    </g>
  </svg>

  <div class="script script-intro-1">Let’s get this</div>
  <div class="script script-intro-2">party started...</div>

  <section class="starters">
    <p class="item" style="top:627px"><span class="item-name">MEXICAN POKE</span>Fresh Ahi Tuna blended w/ spices<br>&amp; ponzu on a bed of colored cabbage</p>
    <p class="item" style="top:762px"><span class="item-name">MERMAID TAILS</span>Shrimp Tempura beached on coconut slaw<br>w/sweet heat glaze, rice pearls, fresh cilantro</p>
    <p class="item" style="top:896px"><span class="item-name">FIESTA NACHOS</span>Crunchy tortilla chips layered w/<br>queso fresco,pickled vegetables, black beans, tomatillo salsa,<br>dry chile salsa &amp; cilantro. As flavorful as it is colorful!<span class="upcharge">*add any protein for upcharge</span></p>
    <p class="item" style="top:1115px"><span class="item-name">ELOTE</span> Roasted corn sliced from the cob, chopped onions<br>and poblano peppers w/ cotija cheese, smoky<br>homemade morita mayo &amp; Rojita</p>
    <p class="item" style="top:1288px"><span class="item-name">GUACAMOLE &amp; CHIPS</span>Smooth blend of Haas avocados,<br>jalapeño, red onions</p>
    <p class="item" style="top:1422px"><span class="item-name">CHIPS AND SALSA</span>Tortilla chips w/ choice of traditional<br>rojo salsa or tomatillo verde</p>
    <p class="item" style="top:1556px"><span class="item-name">QUESO AND CHIPS</span>Melted queso fresco &amp; crunchy tortilla chips</p>
    <p class="item" style="top:1652px"><span class="item-name">RICE &amp; BLACK BEANS</span>Traditional Mexican arroz verde &amp;<br>black beans seasoned w/ epazote</p>
  </section>

  <div class="script script-tacos">Tacos*</div>
  <p class="tacos-note">* All tacos finished Breezy Style with fresh<br>cilantro, side of dry chile salsa &amp; lime wedges</p>

  <section class="tacos">
    <p class="item" style="top:1974px"><span class="item-name">KOREAN</span>Braised short ribs,caramelized onions,<br>cucumber salad, Gochujang sauce</p>
    <p class="item" style="top:2109px"><span class="item-name">BARBACOA</span>Spiced Angus beef, cool creama,<br>white diced onion, tomatillo-avocado salsa</p>
    <p class="item" style="top:2243px"><span class="item-name">AL PASTOR</span>Spit-grilled Heritage Pork, diced white onion,<br>charred pineapple, queso fresco</p>
    <p class="item" style="top:2378px"><span class="item-name">CARNITAS</span>Slow simmered Heritage Pork, avocado smash,<br>pickled red onion, blistered shishito peppers</p>
    <p class="item" style="top:2511px"><span class="item-name">ALABAMA SLAMMA</span>Pulled smoked chicken, Alabama White Sauce,<br>pickled cabbage, fried onions, bacon blanket</p>
    <p class="item" style="top:2645px"><span class="item-name">CHICK NEXT DOOR</span>Grilled chicken breast, elote,<br>avocado smash, queso fresco, salsa verde</p>
  </section>

  <div class="brand-name">Breezy Burro</div>
</main>
</body>
</html>
```